Website and Mobile Devices design for food related application.

We need a design that is simple yet playful. The design should be food related if possible.
This design will be on the website and the mobile platform markets we intend application to be deployed too.
This application/website is called "Bitelora[.com]. Its a random restaurant picker for the indecisive users.
Updates
Hi all, I picked a design. Again lots of great designs were submitted but I picked one that was more in line with what I wanted.
Target Market(s)
young internet savvy users.
Industry/Entity Type
Restaurant
Look and feel
Each slider illustrates characteristics of the customer's brand and the style your logo design should communicate.

```html
<!DOCTYPE html>
<html lang="en">
<head>
<meta charset="utf-8">
<title>Bitelora – random restaurant picker</title>
<link rel="stylesheet" href="https://fonts.googleapis.com/css2?family=Paytone+One&family=Arimo:wght@400;700&display=swap">
<style>
:root{
  --rust:#b95a30;
  --hero-top:#f39449;
  --hero-bottom:#d9692f;
  --brown-dark:#6a3117;
  --panel-light:#9d4f26;
  --panel-dark:#773a1b;
  --yellow:#fbb414;
  --nav-yellow:#ffc31c;
  --body-text:#6a5a52;
  --white:#ffffff;
  --social:#ef8a3a;
}
*{margin:0;padding:0;box-sizing:border-box}
html,body{width:1200px;height:1000px;overflow:hidden;background:var(--white)}
body{position:relative;font-family:"Arimo",Arial,sans-serif;color:var(--body-text)}
.display{font-family:"Paytone One",sans-serif}

.site-header{position:absolute;left:0;top:0;width:1200px;height:68px;background:var(--rust)}
.brand{position:absolute;left:200px;top:14px;font-family:"Paytone One",sans-serif;font-size:28px;color:var(--white);letter-spacing:-.5px}
.main-nav{position:absolute;right:200px;top:20px;display:flex;gap:38px}
.main-nav a{display:flex;align-items:center;gap:6px;font-family:"Paytone One",sans-serif;font-size:17px;color:var(--nav-yellow);text-decoration:none}
.main-nav svg{width:22px;height:22px}

.hero{position:absolute;left:0;top:68px;width:1200px;height:397px;background:linear-gradient(180deg,var(--hero-top),var(--hero-bottom))}
.hero-title{position:absolute;left:200px;top:84px;font-family:"Paytone One",sans-serif;font-style:italic;font-size:54px;line-height:60px;color:var(--brown-dark);letter-spacing:-1px}
.hero-sub{position:absolute;left:200px;top:220px;font-family:"Paytone One",sans-serif;font-size:37px;line-height:42px;color:var(--white);letter-spacing:-.5px}
.hero-illustration{position:absolute;left:425px;top:12px;width:580px;height:385px;background:radial-gradient(ellipse at 62% 55%,#e9e0d8 0,#d9b59a 22%,rgba(233,140,80,0) 55%)}

.intro{position:absolute;left:200px;top:495px;width:800px;font-size:13px;line-height:21.5px;text-align:center}

.panel{position:absolute;top:586px;width:384px}
.panel-left{left:200px}
.panel-right{left:616px}
.panel-title{height:50px;display:flex;align-items:center;justify-content:center;font-family:"Paytone One",sans-serif;font-size:23px;color:var(--white)}
.panel-left .panel-title{background:var(--panel-light)}
.panel-right .panel-title{background:var(--panel-dark)}
.panel-text{margin-top:19px;font-size:13px;line-height:21.5px}
.cuisine-grid{margin-top:20px;display:grid;grid-template-columns:125px 125px 125px;row-gap:15px}
.cuisine{display:flex;align-items:center;gap:6px;font-size:13px}
.checkbox{width:15px;height:15px;border:1.5px solid #6f5f58;border-radius:3px}
.action{position:absolute;top:178px;left:83px;width:209px;height:42px;border-radius:21px;background:var(--yellow);color:var(--white);font-family:"Paytone One",sans-serif;font-size:16px;display:flex;align-items:center;justify-content:center}
.panel-rule{position:absolute;top:241px;left:0;width:384px;height:2px;background:var(--panel-light)}

.closing{position:absolute;left:200px;top:850px;width:800px;font-size:10px;line-height:16px;text-align:center}

.site-footer{position:absolute;left:0;top:909px;width:1200px;height:91px;background:var(--rust)}
.footer-links{position:absolute;left:200px;top:17px;display:flex;gap:15px}
.footer-links a{font-size:10px;color:var(--nav-yellow);text-decoration:none}
.social{position:absolute;right:200px;top:14px;display:flex;gap:6px}
.social span{width:19px;height:19px;background:var(--social);border-radius:2px}
</style>
</head>
<body>
<header class="site-header">
  <div class="brand">Bitelora</div>
  <nav class="main-nav">
    <a href="#"><svg viewBox="0 0 22 22" fill="none" stroke="#fff" stroke-width="1.5"><path d="M3 11 11 3l8 8M5 9v10h12V9M9 19v-5h4v5"/></svg>home</a>
    <a href="#"><svg viewBox="0 0 22 22" fill="none" stroke="#fff" stroke-width="1.5"><path d="M3 4h16v11H9l-4 4v-4H3z"/></svg>contact us</a>
  </nav>
</header>

<section class="hero">
  <div class="hero-illustration" role="img" aria-label="Photo of an indecisive man holding his forehead, with chalk thought bubbles of a pizza slice and a taco"></div>
  <h1 class="hero-title">Tough choice<br>huh?! ...</h1>
  <p class="hero-sub">Well not<br>any more!</p>
</section>

<p class="intro">Lorem ipsum dolor sit amet, consectetur adipisicing elit, sed do eiusmod tempor incididunt ut labore et dolore magna aliqua. Ut enim ad minim veniam, quis nostrud exercitation ullamco laboris nisi ut aliquip ex ea commodo consequat. Duis aute irure dolor in reprehenderit in voluptate velit esse cillum dolore eu fugiat nulla pariatur. Excepteur sint occaecat cupidatat non proident.</p>

<section class="panel panel-left">
  <h2 class="panel-title">I just wanna eat! ...</h2>
  <p class="panel-text">Lorem ipsum dolor sit amet, consectetur adipisicing elit, sed do eiusmod tempor incididunt ut labore et dolore magna aliqua. Ut enim ad minim veniam, quis nostrud exercitation ullamco laboris nisi ut aliquip ex ea commodo consequat.</p>
  <div class="action">find me anything!</div>
  <div class="panel-rule"></div>
</section>

<section class="panel panel-right">
  <h2 class="panel-title">I’m in the mood for ...</h2>
  <div class="cuisine-grid">
    <div class="cuisine"><span class="checkbox"></span>Mexican</div>
    <div class="cuisine"><span class="checkbox"></span>Italian</div>
    <div class="cuisine"><span class="checkbox"></span>Greek</div>
    <div class="cuisine"><span class="checkbox"></span>Portuguese</div>
    <div class="cuisine"><span class="checkbox"></span>Pizza</div>
    <div class="cuisine"><span class="checkbox"></span>Burger</div>
    <div class="cuisine"><span class="checkbox"></span>BBQ</div>
    <div class="cuisine"><span class="checkbox"></span>French</div>
    <div class="cuisine"><span class="checkbox"></span>Jamaican</div>
  </div>
  <div class="action">narrow it down!</div>
  <div class="panel-rule"></div>
</section>

<p class="closing">Dolore magna aliqua. Ut enim ad minim veniam, quis nostrud exercitation ullamco laboris nisi ut aliquip ex ea commodo consequat. Duis aute irure dolor in reprehenderit in voluptate velit esse cillum dolore eu fugiat nulla pariatur. Excepteur sint occaecat cupidatat non proident.</p>

<footer class="site-footer">
  <nav class="footer-links">
    <a href="#">Home</a><a href="#">Contact Us</a><a href="#">Privacy Policy</a><a href="#">Terms &amp; Conditions</a>
  </nav>
  <div class="social" aria-label="Social links"><span></span><span></span></div>
</footer>
</body>
</html>
```